out of the box Business Card Design for a Manufacturer / Distributor

We are a manufarturer and distributor of products.
the company name is VORTANI (Pic attached)

the picture is NOT a must have on the business Card.

the Business Card should look really professional and/or special, so out of the box thinking is welcome.

there should be 2 Adresses on the Business Card for Main and Branch Office.
Email Adress, homepage, Name is required
NO Phone Number

Our working field:
Private Labeling
high Quality Production
direct distribution
warehousing
trademark registration
legal support

Main Office:
Kornblumenweg 14
08352 Eschenfeld
Westmark

Branch Office:
Daska Lane
Qalmora
Eastmark

Names:
Lukas Feldhaus (Owner)
Imran Qureshi (Owner)

Email:
lukas@vortani-example.com
imran@vortani-example.com

homepage:
vortani-example.com

Industry/Entity Type

Manufacturer Distributer

Contact Information for Business Card

Vortani

Requirements
Must have
• Names, both office Adresses, email, homepage
Should not have
• Phone Number

```html
<!DOCTYPE html>
<html lang="en">
<head>
<meta charset="utf-8">
<title>Vortani — Business Card</title>
<link rel="stylesheet" href="https://fonts.googleapis.com/css2?family=Arimo:wght@400;700&display=swap">
<style>
  :root {
    --backdrop: #e4e1db;
    --card: #c9c9c2;
    --ink: #111111;
    --shadow: rgba(40, 30, 20, 0.28);
  }
  * { box-sizing: border-box; margin: 0; padding: 0; }
  html, body {
    width: 1200px;
    height: 900px;
    overflow: hidden;
    background: var(--backdrop);
    font-family: "Arimo", Arial, sans-serif;
    color: var(--ink);
  }
  .canvas {
    position: relative;
    width: 1200px;
    height: 900px;
  }
  .card {
    position: absolute;
    left: 300px;
    width: 600px;
    height: 380px;
    background: var(--card);
    box-shadow: 0 10px 26px var(--shadow);
  }
  .card--front { top: 50px; }
  .card--back { top: 470px; }

  /* Front */
  .front-name {
    position: absolute;
    left: 56px;
    top: 78px;
    font-size: 20px;
    letter-spacing: 1.5px;
    font-weight: 400;
  }
  .front-mark {
    position: absolute;
    right: 90px;
    top: 70px;
    width: 130px;
    height: 130px;
    border-radius: 50%;
    background: var(--ink);
  }

  /* Back */
  .brand {
    position: absolute;
    left: 56px;
    top: 48px;
    display: flex;
    align-items: center;
    gap: 14px;
  }
  .brand-dot {
    width: 44px;
    height: 44px;
    border-radius: 50%;
    background: var(--ink);
  }
  .brand-name {
    font-size: 18px;
    letter-spacing: 1.5px;
  }
  .contact {
    position: absolute;
    font-size: 14px;
    line-height: 1.45;
  }
  .contact-name { font-weight: 700; font-size: 15px; }
  .contact--lukas { left: 56px; top: 226px; }
  .contact--imran { left: 300px; top: 250px; }
  .offices {
    position: absolute;
    left: 56px;
    top: 300px;
    font-size: 14px;
    line-height: 1.55;
  }
  .offices strong { font-weight: 700; }
  .website {
    position: absolute;
    right: 30px;
    top: 190px;
    font-size: 13px;
    font-weight: 700;
    transform: rotate(-90deg);
    transform-origin: right center;
    white-space: nowrap;
  }
</style>
</head>
<body>
  <main class="canvas">
    <section class="card card--front" aria-label="Card front">
      <p class="front-name">VORTANI</p>
      <div class="front-mark" aria-hidden="true"></div>
    </section>

    <section class="card card--back" aria-label="Card back">
      <div class="brand">
        <span class="brand-dot" aria-hidden="true"></span>
        <span class="brand-name">VORTANI</span>
      </div>

      <div class="contact contact--lukas">
        <p class="contact-name">Lukas Feldhaus</p>
        <p class="contact-email">lukas@vortani-example.com</p>
      </div>

      <div class="contact contact--imran">
        <p class="contact-name">Imran Qureshi</p>
        <p class="contact-email">imran@vortani-example.com</p>
      </div>

      <div class="offices">
        <p><strong>Main office:</strong> Kornblumenweg 14, 08352 Eschenfeld, Westmark</p>
        <p><strong>Branch office:</strong> Daska Lane, Qalmora, Eastmark</p>
      </div>

      <p class="website">vortani-example.com</p>
    </section>
  </main>
</body>
</html>
```